make it look old timey and motherly but mordern...bath soak with cooling vapors. tall pine hush

need a bath soak label...cooling vapors. will be in a pouch like below. dont pay attention to the design, just attatching so you know the kind of pouch itll be in. need something trusty, minimal and clean...its called tall pine hush bath soak the best bath yull ever take.... for sore muscles, cooling vapors, smells good...made with menthol lemon and eucalyptus...give me something good.

Target Market(s)

make it look old timey and motherly but mordern

Font styles to use
Serif
Sans Serif

Colors
0054AA
0677BA
7BADD7
CADEEF
E8F1F8
0094D4
00A9DD
6FCCEA
C7EBF8
E9F6FB
FFF300
FFF600
FEFA6F
FFFEC7
FFFEE8
FFC000
F8CF3A
FAE287
FDF2CF
FEFAEE
E54698
E96AAD
F1A4CE
F9D9EA
FCEFF6
6B429C
8869AF
B7A5CE
E3DAEB
F3F0F8

```html
<!DOCTYPE html>
<html lang="en">
<head>
<meta charset="utf-8">
<title>Tall Pine Hush Bath Soak Label</title>
<link href="https://fonts.googleapis.com/css2?family=Big+Shoulders+Display:wght@400;500&family=Mr+Dafoe&family=Questrial&display=swap" rel="stylesheet">
<style>
  :root {
    --pink: #e24a92;
    --coral: #e96a66;
    --orange: #ef8a3e;
    --gold: #fbb90e;
    --tab-yellow: #fcbb05;
    --purple: #6b479a;
    --white: #ffffff;
    --leaf-green: #0f6a35;
    --lemon: #f2ea2a;
    --lemon-pale: #faf6a0;
    --leaf-light: #8fd08a;
    --ink: #1b1410;
  }
  * { margin: 0; padding: 0; box-sizing: border-box; }
  html, body { width: 800px; height: 1200px; overflow: hidden; }
  body { background: #ffffff; }
  .label {
    position: relative;
    width: 800px;
    height: 1200px;
    overflow: hidden;
    background: linear-gradient(180deg, var(--pink) 0%, var(--coral) 35%, var(--orange) 62%, var(--gold) 92%);
  }
  .brand-tab {
    position: absolute;
    left: 273px;
    top: 0;
    width: 199px;
    height: 311px;
    background: var(--tab-yellow);
    border-radius: 0 0 100px 100px;
    display: flex;
    flex-direction: column;
    align-items: center;
    justify-content: flex-end;
    padding-bottom: 86px;
    gap: 12px;
  }
  .brand-name {
    font-family: "Big Shoulders Display", sans-serif;
    font-weight: 500;
    font-size: 30px;
    line-height: 1;
    letter-spacing: 2px;
    color: var(--purple);
    text-transform: uppercase;
    text-align: center;
  }
  .brand-dot {
    width: 14px;
    height: 14px;
    border-radius: 50%;
    background: var(--purple);
  }
  .tagline {
    position: absolute;
    left: 210px;
    top: 330px;
    width: 420px;
    text-align: center;
    font-family: "Mr Dafoe", cursive;
    font-size: 46px;
    color: var(--white);
    transform: rotate(-7deg);
    white-space: nowrap;
  }
  .product-title {
    position: absolute;
    left: 0;
    top: 0;
  }
  .benefit-box {
    position: absolute;
    left: 82px;
    top: 685px;
    width: 639px;
    height: 103px;
    background: var(--purple);
    border-radius: 16px;
  }
  .ingredients {
    position: absolute;
    left: 180px;
    top: 815px;
    width: 440px;
    font-family: "Mr Dafoe", cursive;
    color: var(--leaf-green);
    font-size: 46px;
    line-height: 56px;
    transform: rotate(-7deg);
    white-space: nowrap;
  }
  .ingredients .line-two { display: block; padding-left: 95px; }
  .citrus-art {
    position: absolute;
    top: 811px;
    width: 228px;
    height: 389px;
  }
  .citrus-art.left {
    left: 0;
    background:
      radial-gradient(circle at 20px 260px, var(--lemon-pale) 0 40px, var(--lemon) 90px, #e4e21e 130px, #f8f7c8 136px, transparent 142px),
      radial-gradient(ellipse at 120px 120px, var(--leaf-light) 0, #3f9a45 90px, transparent 140px);
  }
  .citrus-art.right {
    right: 0;
    background:
      radial-gradient(circle at 208px 260px, var(--lemon-pale) 0 40px, var(--lemon) 90px, #e4e21e 130px, #f8f7c8 136px, transparent 142px),
      radial-gradient(ellipse at 108px 120px, var(--leaf-light) 0, #3f9a45 90px, transparent 140px);
  }
  .net-weight {
    position: absolute;
    left: 0;
    width: 800px;
    top: 1154px;
    text-align: center;
    font-family: "Questrial", sans-serif;
    font-size: 21px;
    color: var(--ink);
    letter-spacing: 0.5px;
  }
</style>
</head>
<body>
  <main class="label">
    <div class="brand-tab">
      <span class="brand-name">Tall Pine Hush</span>
      <span class="brand-dot"></span>
    </div>

    <p class="tagline">The best bath yull ever take.</p>

    <div class="benefit-box"></div>

    <svg class="product-title" width="800" height="1200" viewBox="0 0 800 1200">
      <text x="92" y="655" textLength="621" lengthAdjust="spacingAndGlyphs"
            font-family="'Big Shoulders Display', sans-serif" font-weight="400"
            font-size="270" fill="var(--purple)">BATH SOAK</text>
      <text x="105" y="753" textLength="595" lengthAdjust="spacingAndGlyphs"
            font-family="'Big Shoulders Display', sans-serif" font-weight="400"
            font-size="54" fill="var(--white)">for sore muscles, cooling vapors, smells good</text>
    </svg>

    <div class="citrus-art left" role="img" aria-label="Lemon slice with green mint leaves"></div>
    <div class="citrus-art right" role="img" aria-label="Lemon slice with green mint leaves"></div>

    <p class="ingredients">Made with menthol lemon<span class="line-two">and eucalyptus</span></p>

    <p class="net-weight">NET WGT: 15OZ (425G)</p>
  </main>
</body>
</html>
```